Business card for STEADYWAVE

Please design professional business card for IT consulting firm STEADYWAVE INC.
Use logo attached.
Use information from sample qNode business card attached.
replace qnode inc with STEADYWAVE INC.
as well as qnodeinc.com with steadywave.example

```html
<!DOCTYPE html>
<html lang="en">
<head>
<meta charset="utf-8">
<title>STEADYWAVE Business Card</title>
<link href="https://fonts.googleapis.com/css2?family=Roboto+Condensed:wght@700&family=Roboto:wght@400;500;700&display=swap" rel="stylesheet">
<style>
  :root {
    --stage: #2b2b2e;
    --card-white: #ffffff;
    --card-black: #050505;
    --name-purple: #9b12d6;
    --title-orange: #f7941d;
    --text-dark: #3a3a3a;
    --icon-cyan: #29b6f6;
    --band-gradient: linear-gradient(180deg, #38f7c9 0%, #36d3f5 28%, #8c2fe6 52%, #c54b9a 72%, #f39a1a 100%);
    --rule-gradient: linear-gradient(90deg, #9b12d6 0%, #f39a1a 50%, #36d3f5 100%);
  }
  * { box-sizing: border-box; margin: 0; padding: 0; }
  html, body {
    width: 1200px; height: 718px; overflow: hidden;
    background: var(--stage);
  }
  .stage {
    position: relative; width: 1200px; height: 718px;
    display: flex; align-items: center; justify-content: center; gap: 40px;
  }
  .card {
    position: relative; width: 540px; height: 309px; overflow: hidden;
    box-shadow: 0 18px 40px rgba(0,0,0,0.45);
  }
  .card-front { background: var(--card-white); }
  .card-back { background: var(--card-black); }

  .accent-band {
    position: absolute; top: 0; bottom: 0; width: 58px;
    background: var(--band-gradient);
  }
  .card-front .accent-band { right: 0; }
  .card-back .accent-band { left: 48px; }

  .identity { position: absolute; left: 42px; top: 44px; }
  .person-name {
    font-family: "Roboto Condensed", sans-serif; font-weight: 700;
    font-size: 23px; color: var(--name-purple); letter-spacing: 0.2px;
  }
  .person-title {
    font-family: "Roboto", sans-serif; font-weight: 400;
    font-size: 13.5px; color: var(--title-orange); margin-top: 1px;
  }
  .title-rule {
    width: 56px; height: 4px; margin-top: 16px;
    background: var(--rule-gradient);
  }

  .details {
    position: absolute; left: 42px; top: 146px;
    font-family: "Roboto", sans-serif; font-size: 12.5px;
    color: var(--text-dark); line-height: 1.38;
  }
  .detail-row { display: flex; align-items: flex-start; gap: 10px; }
  .detail-row svg { width: 12px; height: 12px; flex: none; margin-top: 3px; fill: var(--icon-cyan); }
  .company-name { font-weight: 700; font-size: 13px; }
  .address-block { margin-bottom: 10px; }

  .wordmark {
    position: absolute; right: 52px; top: 50%; transform: translateY(-50%);
    font-family: "Roboto", sans-serif; font-weight: 500;
    font-size: 30px; letter-spacing: 4px; color: var(--card-white);
  }
</style>
</head>
<body>
<main class="stage">
  <section class="card card-front">
    <div class="identity">
      <h1 class="person-name">DARIA VOLOSHENKO, P.ENG.</h1>
      <p class="person-title">General Manager</p>
      <div class="title-rule"></div>
    </div>

    <div class="details">
      <div class="detail-row address-block">
        <svg viewBox="0 0 24 24" aria-hidden="true"><path d="M12 1a8 8 0 0 0-8 8c0 6 8 14 8 14s8-8 8-14a8 8 0 0 0-8-8zm0 11a3 3 0 1 1 0-6 3 3 0 0 1 0 6z"/></svg>
        <div>
          <div class="company-name">STEADYWAVE INC.</div>
          <div>1280 Harbourline Rd., Suite 204</div>
          <div>Oakridge, Ontario</div>
          <div>K2P 4R8, Canada</div>
        </div>
      </div>
      <div class="detail-row">
        <svg viewBox="0 0 24 24" aria-hidden="true"><path d="M6.6 10.8a15 15 0 0 0 6.6 6.6l2.2-2.2a1 1 0 0 1 1-.25 11.4 11.4 0 0 0 3.6.57 1 1 0 0 1 1 1V20a1 1 0 0 1-1 1A17 17 0 0 1 3 4a1 1 0 0 1 1-1h3.5a1 1 0 0 1 1 1c0 1.25.2 2.45.57 3.6a1 1 0 0 1-.25 1z"/></svg>
        <span>(555) 014-2730 ext.118</span>
      </div>
      <div class="detail-row">
        <svg viewBox="0 0 24 24" aria-hidden="true"><path d="M7 1h10a2 2 0 0 1 2 2v18a2 2 0 0 1-2 2H7a2 2 0 0 1-2-2V3a2 2 0 0 1 2-2zm0 3v14h10V4zm5 15.5a1.2 1.2 0 1 0 0 2.4 1.2 1.2 0 0 0 0-2.4z"/></svg>
        <span>(555) 019-4482</span>
      </div>
      <div class="detail-row">
        <svg viewBox="0 0 24 24" aria-hidden="true"><path d="M2 5h20v14H2zm2 2v.5l8 5 8-5V7zm0 2.9V17h16V9.9l-8 5z"/></svg>
        <span>dvoloshenko@steadywave.example</span>
      </div>
      <div class="detail-row">
        <svg viewBox="0 0 24 24" aria-hidden="true"><path d="M12 2a10 10 0 1 0 0 20 10 10 0 0 0 0-20zm-1 17.9A8 8 0 0 1 4.2 10L9 14.8v1a2 2 0 0 0 2 2zm6.9-2.5A2 2 0 0 0 16 16h-1v-3a1 1 0 0 0-1-1H8v-2h2a1 1 0 0 0 1-1V7h2a2 2 0 0 0 2-2v-.4a8 8 0 0 1 2.9 12.8z"/></svg>
        <span>www.steadywave.example</span>
      </div>
    </div>

    <div class="accent-band"></div>
  </section>

  <section class="card card-back">
    <div class="accent-band"></div>
    <p class="wordmark">STEADYWAVE</p>
  </section>
</main>
</body>
</html>
```